Business Card Design

Velvet Pixel Promotions

An online marketing consulting & strategy business for the cosmetic niche

We specialise in Increasing Leads, Conversions & Content Marketing

I am looking for a very clean, BOLD business card that is simple & effective

Target Market(s)

cosmetic surgeons & cosmetic clinics

Industry/Entity Type

Marketing

Contact Information for Business Card

Darren Okoye
Online Marketing Strategist

Darren@VelvetPixelPromotions.example
0491 268 517

LinkedIn: in/darrenokoye

```html
<!DOCTYPE html>
<html lang="en">
<head>
<meta charset="utf-8">
<title>Velvet Pixel Promotions – Business Card</title>
<link rel="stylesheet" href="https://fonts.googleapis.com/css2?family=Exo+2:wght@600&display=swap">
<style>
  :root {
    --paper: #ffffff;
    --ink: #5a6369;
    --lime: #8fe03a;
    --aqua: #5fd3e0;
    --aqua-soft: #c4f0f3;
  }
  html, body {
    margin: 0;
    padding: 0;
    overflow: hidden;
    background: var(--paper);
  }
  .card {
    position: relative;
    width: 1200px;
    height: 741px;
    background: var(--paper);
    overflow: hidden;
  }
  .swoosh-area {
    position: absolute;
    left: 103px;
    top: 103px;
    width: 1097px;
    height: 400px;
    border-radius: 50% 0 0 50% / 50% 0 0 50%;
    background: linear-gradient(100deg, rgba(143, 224, 58, 0.10) 0%, rgba(95, 211, 224, 0.10) 45%, rgba(196, 240, 243, 0.06) 100%);
  }
  .speed-area {
    position: absolute;
    left: 411px;
    top: 443px;
    width: 540px;
    height: 195px;
    border-radius: 0 60% 0 0 / 0 100% 0 0;
    background: linear-gradient(90deg, rgba(143, 224, 58, 0.45) 0%, rgba(95, 211, 224, 0.40) 55%, rgba(95, 211, 224, 0) 100%);
  }
  .brand-mark {
    position: absolute;
    left: 203px;
    top: 273px;
    width: 140px;
    height: 140px;
    box-sizing: border-box;
    border: 10px solid var(--aqua);
    border-radius: 50%;
  }
  .brand-name {
    position: absolute;
    left: 373px;
    top: 266px;
    margin: 0;
    font-family: "Exo 2", sans-serif;
    font-weight: 600;
    font-size: 54px;
    line-height: 56px;
    color: var(--ink);
    text-transform: uppercase;
    white-space: nowrap;
  }
  .brand-name span {
    display: block;
  }
  .brand-name .line-one { letter-spacing: 40px; }
  .brand-name .line-two { letter-spacing: 61px; }
  .brand-name .line-three { letter-spacing: 4px; }
</style>
</head>
<body>
  <main class="card">
    <div class="swoosh-area" role="img" aria-label="Sweeping swoosh arc in aqua and lime"></div>
    <div class="speed-area" role="img" aria-label="Lime to aqua speed streaks"></div>
    <div class="brand-mark"></div>
    <h1 class="brand-name">
      <span class="line-one">Velvet</span>
      <span class="line-two">Pixel</span>
      <span class="line-three">Promotions</span>
    </h1>
  </main>
</body>
</html>
```